Vell Tarnmoor - Brochure - Industrial Construction Services

We need a brochure design based on the power point presentation attached. Our business is named Vell Tarnmoor and is an industrial project services business concentrating on Construction Project Management, Technical Services, and Consulting. We want to communicate that "We offer our clients a
unique systematic approach to solving technical challenges." As you can see from our logo designs we like the colors blue and grey. We are after clean, but innovative design overall. We also seem to like design that have darker style backgrounds. We would like this brochure to be a bi-fold 8.5"x 5.5" size when closed if possible. If any files or graphics are needed in original format please request them. Thanks!

Target Market(s)

Large Oil & Gas, Power Generation, and Engineering Companies.

Industry/Entity Type

Engineering

Font styles to use
Serif

Requirements
Must have
• A strong-lasting first impression.

```html
<!DOCTYPE html>
<html lang="en">
<head>
<meta charset="utf-8">
<title>Vell Tarnmoor – Brochure Spreads</title>
<link href="https://fonts.googleapis.com/css2?family=Libre+Baskerville:wght@400;700&family=Tinos:wght@400;700&display=swap" rel="stylesheet">
<style>
  :root{
    --navy:#1c1f5e;
    --royal:#2f4596;
    --strip:#c9ced9;
    --ink:#1b1d3a;
    --teal:#1f6f8b;
    --teal-line:#2a7f9c;
    --box-blue:#a9d3df;
    --box-border:#3b6f80;
    --gold:#f9c84a;
    --gold-border:#c48a12;
    --panel-line:#9fc6ea;
    --canvas:#e6e7ea;
  }
  *{box-sizing:border-box;margin:0;padding:0}
  html,body{width:1200px;height:1200px;overflow:hidden}
  body{background:var(--canvas);font-family:"Tinos",serif;color:var(--ink);position:relative}

  .spread{position:absolute;left:20px;width:1160px;height:430px;display:flex;box-shadow:0 6px 18px rgba(0,0,0,.18)}
  .spread--upper{top:90px}
  .spread--lower{top:680px}
  .page{position:relative;width:580px;height:430px;background:linear-gradient(90deg,#fff 0%,#f7f7f9 100%);overflow:hidden}
  .page--right{background:linear-gradient(90deg,#eeeff2 0%,#fff 8%,#fff 100%)}

  .page-header{position:absolute;left:0;top:0;width:580px;height:72px}
  .page-header svg{position:absolute;inset:0}
  .page-title{position:absolute;left:32px;top:24px;font-family:"Libre Baskerville",serif;font-weight:700;font-size:22px;color:#fff;letter-spacing:.5px}
  .brand{position:absolute;left:420px;top:26px;display:flex;align-items:center;gap:6px;font-family:"Libre Baskerville",serif;font-size:11px;color:#fff}
  .brand-dot{width:18px;height:18px;border-radius:50%;border:2px solid #dfe3ee}

  .page-footer{position:absolute;top:400px;left:0;width:100%;text-align:center;font-size:8px;letter-spacing:2px;color:#333}
  .page-num{position:absolute;top:384px;font-family:"Libre Baskerville",serif;font-size:15px;font-weight:700;color:var(--ink);border-bottom:3px solid var(--teal);padding:0 2px 1px}
  .page--left .page-num{left:34px}
  .page--right .page-num{right:36px}

  /* management org panel */
  .org-panel{position:absolute;left:35px;top:77px;width:473px;height:308px;border-radius:10px;background:linear-gradient(180deg,#1f2570 0%,#262c7c 100%);box-shadow:inset 0 0 0 2px #10144a}
  .org-panel svg.links{position:absolute;inset:0}
  .org-brand{position:absolute;left:16px;top:14px;display:flex;align-items:center;gap:6px;font-family:"Libre Baskerville",serif;font-size:12px;color:#fff}
  .org-caption{position:absolute;left:20px;top:56px;font-family:"Libre Baskerville",serif;font-size:10.5px;font-weight:700;color:#fff;text-decoration:underline}
  .role-box{position:absolute;background:linear-gradient(180deg,#e9f2fb 0%,#7fb2df 100%);border:1px solid #c8def2;color:var(--ink)}
  .role-box h4{font-family:"Libre Baskerville",serif;font-size:8.5px;font-weight:700;padding:3px 6px;background:linear-gradient(180deg,#fff 0%,#cfe2f3 100%);border-bottom:1px solid #8db4d8;white-space:nowrap}
  .role-box ul{list-style:disc;padding:3px 6px 0 18px;font-size:7.2px;line-height:10px}
  .role-tech{left:58px;top:82px;width:120px;height:88px}
  .role-lead{left:220px;top:6px;width:125px;height:92px}
  .role-lead h4{font-size:10px;background:none;border:none}
  .role-controls{left:380px;top:8px;width:113px;height:66px}
  .role-logistics{left:380px;top:84px;width:113px;height:92px}

  .discipline-row{position:absolute;left:18px;top:188px;display:flex;gap:1px}
  .discipline{width:54.6px}
  .discipline-head{height:52px;display:flex;align-items:center;justify-content:center;text-align:center;font-size:8.5px;line-height:10px;background:linear-gradient(180deg,#f3f4f7 0%,#c7ccd6 100%);border:1px solid #9aa3b4;color:#222}
  .discipline-list{height:52px;margin-top:2px;background:linear-gradient(180deg,#e3effa 0%,#8cbbe2 100%);border:1px solid #c2d9ef;font-size:6.8px;line-height:9px;padding:4px 2px 0 3px;color:#111}
  .discipline--faded{opacity:.55}

  /* technical pages */
  .section-heading{position:absolute;font-family:"Libre Baskerville",serif;font-weight:700;color:var(--ink);letter-spacing:1px}
  .check-list{position:absolute;list-style:none;font-size:10.5px;line-height:14.2px;color:#222}
  .check-list li{position:relative;padding-left:21px}
  .check-list li::before{content:"";position:absolute;left:4px;top:2px;width:4px;height:8px;border-right:2px solid var(--navy);border-bottom:2px solid var(--navy);transform:rotate(40deg)}
  .check-list--compact{font-size:10px;line-height:13.6px}
  .photo{position:absolute;border:1px solid #fff}

  .org-title{position:absolute;left:18px;top:95px;font-family:"Libre Baskerville",serif;font-style:italic;font-weight:700;font-size:12px;color:var(--ink);text-decoration:underline}
  .chart{position:absolute;inset:0}
  .chart text{font-family:"Tinos",serif;font-size:7px;fill:#234;text-anchor:middle}
</style>
</head>
<body>

<!-- upper spread: pages 8 & 9 -->
<section class="spread spread--upper">
  <article class="page page--left">
    <header class="page-header">
      <svg width="580" height="72" viewBox="0 0 580 72">
        <defs><linearGradient id="hdrA" x1="0" x2="1"><stop offset="0" stop-color="#2b3f8e"/><stop offset="1" stop-color="#4a66b8"/></linearGradient></defs>
        <polygon points="0,0 330,0 385,72 0,72" fill="var(--navy)"/>
        <polygon points="330,0 346,0 401,72 385,72" fill="var(--strip)"/>
        <polygon points="346,0 580,0 580,72 401,72" fill="url(#hdrA)"/>
      </svg>
      <h2 class="page-title">MANAGEMENT</h2>
      <div class="brand"><span class="brand-dot"></span>Vell Tarnmoor</div>
    </header>

    <div class="org-panel">
      <svg class="links" width="473" height="308" viewBox="0 0 473 308">
        <g stroke="var(--panel-line)" stroke-width="4" fill="none">
          <polyline points="178,120 205,120 205,186"/>
          <line x1="282" y1="98" x2="282" y2="186"/>
          <line x1="345" y1="40" x2="380" y2="40"/>
          <polyline points="362,40 362,128 380,128"/>
          <line x1="100" y1="172" x2="100" y2="186"/>
        </g>
      </svg>
      <div class="org-brand"><span class="brand-dot"></span>Vell Tarnmoor</div>
      <p class="org-caption">Position / Title Examples</p>

      <div class="role-box role-tech">
        <h4>Technical Lead</h4>
        <ul><li>Project Engineers</li><li>Construction Engineers</li><li>Equipment/Package</li><li>Specialist</li><li>Constructability</li><li>Coordinator</li></ul>
      </div>
      <div class="role-box role-lead">
        <h4>Project Leadership</h4>
        <ul><li>Program Manager</li><li>Project Director</li><li>Construction Manager</li><li>Project Manager</li><li>Site Manager</li><li>Implementation Mgr.</li></ul>
      </div>
      <div class="role-box role-controls">
        <h4>Project Controls Lead</h4>
        <ul><li>Cost Engineers</li><li>Schedulers</li><li>Estimators</li><li>Planners</li></ul>
      </div>
      <div class="role-box role-logistics">
        <h4>Logistics Lead</h4>
        <ul><li>Procurement Specialist</li><li>Materials Coordinators</li><li>Logistics Coordinators</li><li>Project Administrative</li><li>Support</li><li>Lodging &amp; Catering</li></ul>
      </div>

      <div class="discipline-row">
        <div class="discipline"><div class="discipline-head">Safety<br>Manager</div><div class="discipline-list">• Lead<br>Inspectors<br>• Field-<br>Coordinators</div></div>
        <div class="discipline"><div class="discipline-head">QA/QC<br>Manager</div><div class="discipline-list">• Lead<br>Inspectors<br>• Field-<br>Coordinators</div></div>
        <div class="discipline"><div class="discipline-head">Civil/<br>Structural<br>Manager</div><div class="discipline-list">• Lead<br>Inspectors<br>• Field-<br>Coordinators</div></div>
        <div class="discipline"><div class="discipline-head">Mechanical<br>Manager</div><div class="discipline-list">• Lead<br>Inspectors<br>• Field-<br>Coordinators</div></div>
        <div class="discipline"><div class="discipline-head">Heavy-Lift<br>Manager</div><div class="discipline-list">• Lead<br>Inspectors<br>• Field-<br>Coordinators</div></div>
        <div class="discipline"><div class="discipline-head">Piping<br>Manager</div><div class="discipline-list">• Lead<br>Inspectors<br>• Field-<br>Coordinators</div></div>
        <div class="discipline"><div class="discipline-head">Electrical/<br>Instrument<br>Manager</div><div class="discipline-list">• Lead<br>Inspectors<br>• Field-<br>Coordinators</div></div>
        <div class="discipline discipline--faded"><div class="discipline-head" style="font-size:7px">Commissioning<br>Start-up<br>Manager</div><div class="discipline-list">• Lead<br>Inspectors<br>• Field-<br>Coordinators</div></div>
      </div>
    </div>

    <p class="page-footer">WWW.VELLTARNMOOR.COM</p>
    <span class="page-num">8</span>
  </article>

  <article class="page page--right">
    <header class="page-header">
      <svg width="580" height="72" viewBox="0 0 580 72">
        <defs><linearGradient id="hdrB" x1="0" x2="1"><stop offset="0" stop-color="#2b3f8e"/><stop offset="1" stop-color="#4a66b8"/></linearGradient></defs>
        <polygon points="0,0 330,0 385,72 0,72" fill="var(--navy)"/>
        <polygon points="330,0 346,0 401,72 385,72" fill="var(--strip)"/>
        <polygon points="346,0 580,0 580,72 401,72" fill="url(#hdrB)"/>
      </svg>
      <h2 class="page-title">TECHNICAL</h2>
      <div class="brand"><span class="brand-dot"></span>Vell Tarnmoor</div>
    </header>

    <h3 class="section-heading" style="left:18px;top:82px;font-size:15px">Instrumentation &amp; Electrical Technicians</h3>
    <ul class="check-list" style="left:20px;top:118px">
      <li>Complete Field Services</li>
      <li>Calibration &amp; Testing</li>
      <li>Analytical Specialists – Process Analyzers</li>
      <li>Automation Integration</li>
      <li>Construction (TSLB 40826)</li>
      <li>Metering</li>
      <li>Fabrication</li>
    </ul>

    <div class="photo" role="img" aria-label="Instrumentation products: analyzers, transmitters and control enclosures" style="left:245px;top:100px;width:320px;height:125px;border:none;background:radial-gradient(ellipse at 60% 50%,#c9ced6 0%,#eef0f3 70%,#fff 100%)"></div>
    <div class="photo" role="img" aria-label="Multimeter testing a terminal block" style="left:15px;top:243px;width:105px;height:100px;background:linear-gradient(135deg,#8a7a3c,#5e6470)"></div>
    <div class="photo" role="img" aria-label="Electrical terminal block assembly" style="left:110px;top:290px;width:85px;height:78px;background:linear-gradient(135deg,#c9ccd2,#7d8a9c)"></div>
    <div class="photo" role="img" aria-label="Process plant with piping" style="left:118px;top:220px;width:140px;height:85px;background:linear-gradient(180deg,#b9c7d6,#8b98a6)"></div>
    <div class="photo" role="img" aria-label="Electrical switchgear room" style="left:195px;top:262px;width:95px;height:100px;background:linear-gradient(180deg,#c6c9cc,#8e9297)"></div>
    <div class="photo" role="img" aria-label="Instrument piping manifold" style="left:258px;top:243px;width:135px;height:100px;background:linear-gradient(135deg,#6f8a70,#a7a9a0)"></div>
    <div class="photo" role="img" aria-label="Technician wiring a control panel" style="left:350px;top:270px;width:110px;height:108px;background:linear-gradient(135deg,#7e8a99,#3e4f6e)"></div>
    <div class="photo" role="img" aria-label="Control cabinets in a plant room" style="left:458px;top:190px;width:107px;height:165px;background:linear-gradient(180deg,#8f969e,#5c6470)"></div>

    <p class="page-footer">WWW.VELLTARNMOOR.COM</p>
    <span class="page-num">9</span>
  </article>
</section>

<!-- lower spread: pages 10 & 11 -->
<section class="spread spread--lower">
  <article class="page page--left">
    <header class="page-header">
      <svg width="580" height="72" viewBox="0 0 580 72">
        <defs><linearGradient id="hdrC" x1="0" x2="1"><stop offset="0" stop-color="#2b3f8e"/><stop offset="1" stop-color="#4a66b8"/></linearGradient></defs>
        <polygon points="0,0 330,0 385,72 0,72" fill="var(--navy)"/>
        <polygon points="330,0 346,0 401,72 385,72" fill="var(--strip)"/>
        <polygon points="346,0 580,0 580,72 401,72" fill="url(#hdrC)"/>
      </svg>
      <h2 class="page-title">TECHNICAL</h2>
      <div class="brand"><span class="brand-dot"></span>Vell Tarnmoor</div>
    </header>

    <h3 class="section-heading" style="left:32px;top:84px;font-size:13.5px;line-height:22px;letter-spacing:.6px">Turnkey Commissioning/Completions<br>(All Disciplines)</h3>
    <ul class="check-list check-list--compact" style="left:34px;top:130px">
      <li>Planning</li>
      <li>Fabrication QA</li>
      <li>Mechanical Completion</li>
      <li>Pre-Commissioning (Static)</li>
      <li>Commissioning &amp; Startup (Dynamic)</li>
      <li>Complete Database &amp; Databooks</li>
    </ul>

    <svg width="580" height="430" viewBox="0 0 580 430" style="position:absolute;inset:0">
      <g stroke="var(--teal-line)" stroke-width="3" fill="none">
        <polyline points="392,78 392,226 206,226 206,292"/>
        <line x1="32" y1="286" x2="212" y2="286"/>
      </g>
    </svg>
    <div class="photo" role="img" aria-label="Engineer reviewing data on a laptop in a plant" style="left:398px;top:72px;width:166px;height:128px;background:linear-gradient(135deg,#9aa4ad,#5f6b78)"></div>
    <div class="photo" role="img" aria-label="Control panel with indicator lights" style="left:398px;top:205px;width:166px;height:88px;background:linear-gradient(135deg,#7e8b7c,#4f5a63)"></div>
    <div class="photo" role="img" aria-label="Crew walking through a switchgear hall" style="left:398px;top:296px;width:166px;height:95px;background:linear-gradient(180deg,#a8adb2,#6a7078)"></div>
    <div class="photo" role="img" aria-label="Technicians at electrical cabinets" style="left:218px;top:236px;width:172px;height:158px;background:linear-gradient(135deg,#8c949c,#4f5863)"></div>
    <div class="photo" role="img" aria-label="Hands testing cables with a meter" style="left:36px;top:292px;width:176px;height:102px;background:linear-gradient(135deg,#b79a56,#5b6676)"></div>

    <p class="page-footer" style="top:404px">WWW.VELLTARNMOOR.COM</p>
    <span class="page-num" style="top:386px">10</span>
  </article>

  <article class="page page--right">
    <header class="page-header">
      <svg width="580" height="72" viewBox="0 0 580 72">
        <defs><linearGradient id="hdrD" x1="0" x2="1"><stop offset="0" stop-color="#2b3f8e"/><stop offset="1" stop-color="#4a66b8"/></linearGradient></defs>
        <polygon points="0,0 330,0 385,72 0,72" fill="var(--navy)"/>
        <polygon points="330,0 346,0 401,72 385,72" fill="var(--strip)"/>
        <polygon points="346,0 580,0 580,72 401,72" fill="url(#hdrD)"/>
      </svg>
      <h2 class="page-title">TECHNICAL</h2>
      <div class="brand"><span class="brand-dot"></span>Vell Tarnmoor</div>
    </header>

    <p class="org-title">Completions Org. Chart</p>

    <svg class="chart" width="580" height="430" viewBox="0 0 580 430">
      <defs>
        <g id="techColumn">
          <g stroke="var(--teal-line)" stroke-width="2" fill="none">
            <polyline points="-7,305 -7,365 -3,365"/>
            <line x1="-7" y1="330" x2="-3" y2="330"/>
          </g>
          <rect x="-15" y="280" width="30" height="25" fill="var(--box-blue)" stroke="var(--box-border)" stroke-width="1.2"/>
          <text x="0" y="290">Sr.</text><text x="0" y="299">Tech</text>
          <rect x="-3" y="318" width="34" height="24" fill="var(--box-blue)" stroke="var(--box-border)" stroke-width="1.2"/>
          <text x="14" y="333">Tech</text>
          <rect x="-3" y="353" width="34" height="24" fill="var(--box-blue)" stroke="var(--box-border)" stroke-width="1.2"/>
          <text x="14" y="368">Tech</text>
        </g>
      </defs>

      <rect x="170" y="78" width="128" height="133" rx="9" fill="#d4d6da"/>
      <g stroke="var(--teal-line)" stroke-width="2" fill="none">
        <line x1="215" y1="118" x2="215" y2="138"/>
        <line x1="215" y1="173" x2="215" y2="222"/>
        <line x1="215" y1="190" x2="235" y2="190"/>
        <line x1="105" y1="222" x2="389" y2="222"/>
        <line x1="105" y1="222" x2="105" y2="232"/>
        <line x1="249" y1="222" x2="249" y2="232"/>
        <line x1="389" y1="222" x2="389" y2="232"/>
        <line x1="365" y1="160" x2="455" y2="160"/>
        <line x1="397" y1="125" x2="397" y2="160"/>
        <line x1="455" y1="100" x2="455" y2="242"/>
        <line x1="455" y1="100" x2="466" y2="100"/>
        <line x1="455" y1="145" x2="466" y2="145"/>
        <line x1="455" y1="193" x2="466" y2="193"/>
        <line x1="455" y1="242" x2="466" y2="242"/>
      </g>
      <polyline points="250,100 330,100 330,140" stroke="var(--navy)" stroke-width="1.5" stroke-dasharray="2 2" fill="none"/>

      <g fill="var(--box-blue)" stroke="var(--box-border)" stroke-width="1.2">
        <rect x="180" y="83" width="70" height="35"/>
        <rect x="180" y="138" width="70" height="35"/>
        <rect x="235" y="178" width="58" height="28"/>
        <rect x="78" y="232" width="55" height="35"/>
        <rect x="222" y="232" width="55" height="35"/>
        <rect x="362" y="232" width="55" height="35"/>
      </g>
      <text x="215" y="94">Completions &amp;</text><text x="215" y="103">Commissioning</text><text x="215" y="112">Manager</text>
      <text x="215" y="152">Site Completions</text><text x="215" y="162">Lead</text>
      <text x="264" y="189">Database</text><text x="264" y="198">Clerk</text>
      <text x="105" y="247">Mechanical</text><text x="105" y="257">Lead</text>
      <text x="249" y="247">Electrical</text><text x="249" y="257">Lead</text>
      <text x="389" y="247">Controls</text><text x="389" y="257">Lead</text>

      <g fill="var(--gold)" stroke="var(--gold-border)" stroke-width="1.2">
        <rect x="378" y="85" width="38" height="40"/>
        <rect x="300" y="140" width="65" height="40"/>
        <rect x="466" y="83" width="90" height="35"/>
        <rect x="466" y="128" width="90" height="35"/>
        <rect x="466" y="176" width="90" height="35"/>
        <rect x="466" y="224" width="90" height="35"/>
      </g>
      <text x="397" y="98">QA</text><text x="397" y="107">Data</text><text x="397" y="116">Clerk</text>
      <text x="332" y="155">Quality</text><text x="332" y="164">Assurance</text><text x="332" y="173">Lead</text>
      <text x="511" y="98">Procurement</text><text x="511" y="108">QA Lead</text>
      <text x="511" y="143">Civil &amp; Structural</text><text x="511" y="153">QA Lead</text>
      <text x="511" y="191">Piping &amp; Mech</text><text x="511" y="201">QA Lead</text>
      <text x="511" y="239">E&amp;I</text><text x="511" y="249">QA Lead</text>

      <g stroke="var(--teal-line)" stroke-width="2" fill="none">
        <line x1="105" y1="267" x2="105" y2="272"/><line x1="58" y1="272" x2="152" y2="272"/>
        <line x1="249" y1="267" x2="249" y2="272"/><line x1="202" y1="272" x2="296" y2="272"/>
        <line x1="389" y1="267" x2="389" y2="272"/><line x1="342" y1="272" x2="436" y2="272"/>
        <line x1="58" y1="272" x2="58" y2="280"/><line x1="105" y1="272" x2="105" y2="280"/><line x1="152" y1="272" x2="152" y2="280"/>
        <line x1="202" y1="272" x2="202" y2="280"/><line x1="249" y1="272" x2="249" y2="280"/><line x1="296" y1="272" x2="296" y2="280"/>
        <line x1="342" y1="272" x2="342" y2="280"/><line x1="389" y1="272" x2="389" y2="280"/><line x1="436" y1="272" x2="436" y2="280"/>
      </g>

      <use href="#techColumn" x="58"/>
      <use href="#techColumn" x="105"/>
      <use href="#techColumn" x="152"/>
      <use href="#techColumn" x="202"/>
      <use href="#techColumn" x="249"/>
      <use href="#techColumn" x="296"/>
      <use href="#techColumn" x="342"/>
      <use href="#techColumn" x="389"/>
      <use href="#techColumn" x="436"/>
    </svg>

    <p class="page-footer">WWW.VELLTARNMOOR.COM</p>
    <span class="page-num">11</span>
  </article>
</section>

</body>
</html>
```